Webiste Design KLV

Design the website using uploaded content. Design colors should match that of the company logo with an allowance of one more extra color if it makes the website look much better and colorful. Use Technology related stock images in your design.

Target Market(s)

Potential Clients - Companies

Industry/Entity Type

Information Technology

Coding

Coded - Design and coding required

Number of Pages Required

5+ page

Requirements
Must have
• Company Logo Colors
Nice to have
• Professional Look and Feel with Sliders showing professional information technology images

```html
<!DOCTYPE html>
<html lang="en">
<head>
<meta charset="utf-8">
<title>KLV Technologies</title>
<link href="https://fonts.googleapis.com/css2?family=Montserrat:wght@300;400;500;600;700;800&family=Arimo:wght@400;700&display=swap" rel="stylesheet">
<style>
:root{
  --orange:#f7890f;
  --orange-deep:#e87a05;
  --black:#000;
  --ink:#111;
  --white:#fff;
  --grey:#9a9a9a;
  --band:#f0f0f0;
  --field:#e9e9e9;
}
*{margin:0;padding:0;box-sizing:border-box}
html,body{width:1200px;height:4501px;overflow:hidden;background:var(--white)}
body{position:relative;font-family:"Arimo",Arial,sans-serif;color:var(--ink)}
.abs{position:absolute}
.brand{display:flex;align-items:center;gap:12px}
.brand-dot{width:40px;height:40px;border-radius:50%;background:var(--orange)}
.brand-text{font-family:"Montserrat",sans-serif;font-weight:700;color:var(--orange);line-height:1}
.brand-text .name{font-size:46px;letter-spacing:2px}
.brand-text .sub{font-size:13px;letter-spacing:6px;display:block;margin-top:2px}
.site-logo{left:462px;top:18px}
.topbar{left:0;top:94px;width:1200px;height:27px;background:var(--black);color:var(--white);font-size:15px}
.topbar .mail{left:20px;top:5px;display:flex;align-items:center;gap:8px}
.topbar .menu{left:333px;top:5px;display:flex;gap:22px}
.topbar .quote{left:910px;top:4px;width:121px;height:19px;background:var(--orange);border-radius:3px;text-align:center;font-size:14px;line-height:19px;color:var(--black)}
.topbar .phone{left:1052px;top:5px;display:flex;align-items:center;gap:6px}
.subbar{left:0;top:121px;width:1200px;height:27px;background:var(--orange)}
.subbar .tab{top:4px;height:19px;background:var(--white);font-size:13px;line-height:19px;text-align:center;color:var(--ink)}
.hero{left:0;top:148px;width:1200px;height:524px;background:radial-gradient(ellipse at 80% 55%,#f39a2a 0%,#b85a15 25%,#3a2418 60%,#1c1614 100%)}
.hero-social{left:66px;top:163px;display:flex;gap:14px}
.hero-social span{width:18px;height:18px;border-radius:50%;background:var(--orange)}
.hero-box{left:66px;top:293px;width:860px;height:175px;background:rgba(90,80,72,.55);padding:4px 0 0 0}
.hero-box h1{font-family:"Montserrat",sans-serif;font-weight:800;font-size:45px;line-height:58px;color:var(--orange)}
.hero-box p{color:var(--white);font-size:20px;line-height:26px;margin-left:3px}
.card{top:557px;width:237px;height:192px;background:var(--orange);border-radius:3px;text-align:center;color:var(--black)}
.card .art{width:110px;height:90px;margin:30px auto 0;background:linear-gradient(#2a1a0e,#5a3410);border-radius:6px}
.card h3{font-weight:400;font-size:19px;margin-top:14px}
.card em{font-size:13px;color:var(--white)}
.section-title{font-family:"Montserrat",sans-serif;font-weight:400;font-size:44px;color:var(--orange);text-align:center;width:1200px;left:0}
.thought-copy{left:175px;top:873px;width:860px;font-size:14px;line-height:20px;text-align:justify;text-align-last:center}
.governance{left:0;top:1006px;width:1200px;height:1155px;background:var(--black)}
.gov-copy{left:180px;top:1130px;width:850px;font-size:14px;line-height:21px;color:var(--white);text-align:center}
.value{width:220px;height:220px;border-radius:50%;background:var(--orange);display:flex;align-items:center;justify-content:center;text-align:center;font-family:"Montserrat",sans-serif;font-weight:800;font-size:25px;line-height:25px;color:var(--black)}
.value-copy{font-family:"Montserrat",sans-serif;font-weight:500;font-size:17px;line-height:21px;color:var(--orange)}
.partners-band{left:0;top:2311px;width:1200px;height:135px;background:var(--band)}
.badge{top:2341px;height:66px;background:#dcdcdc;border-radius:4px}
.competence{left:0;top:2512px;width:1200px;height:1038px;background:var(--black)}
.comp-lead{font-weight:400;font-size:21px;line-height:26px;color:var(--orange)}
.comp-list{list-style:none;font-size:14px;line-height:26px;color:var(--white)}
.photo{border-radius:50%}
.write{left:177px;top:3715px;font-family:"Montserrat",sans-serif;font-size:40px;color:var(--orange)}
.write-copy{left:177px;top:3773px;width:440px;font-family:"Montserrat",sans-serif;font-size:15px;line-height:21px;color:var(--orange)}
.form{left:666px;top:3621px;width:375px;height:441px;border:4px solid var(--orange);border-radius:3px}
.field{left:702px;width:306px;height:35px;background:var(--field);font-family:"Montserrat",sans-serif;font-size:19px;color:#555;padding:6px 8px}
.footer{left:0;top:4120px;width:1200px;height:317px;background:var(--black)}
.foot-logo{left:129px;top:4179px}
.foot-logo .brand-dot{width:30px;height:30px}
.foot-logo .name{font-size:40px}
.foot-logo .sub{font-size:11px;letter-spacing:5px}
.foot-contact{left:130px;top:4258px;font-family:"Montserrat",sans-serif;font-size:16px;line-height:28px;color:var(--white)}
.foot-social{left:131px;top:4339px;display:flex;gap:22px}
.foot-social span{width:28px;height:28px;border-radius:50%;background:var(--orange)}
.region{font-family:"Montserrat",sans-serif;color:#8c8c8c}
.region h4{font-weight:400;font-size:32px;letter-spacing:1px;margin-bottom:10px}
.region p{font-size:19px;line-height:23px;margin-bottom:23px}
.copyright{left:0;top:4437px;width:1200px;height:64px;text-align:center;line-height:64px;font-family:"Montserrat",sans-serif;font-size:19px;color:#777}
</style>
</head>
<body>

<header>
  <div class="abs brand site-logo">
    <span class="brand-dot"></span>
    <span class="brand-text"><span class="name">KLV</span><span class="sub">TECHNOLOGIES</span></span>
  </div>

  <nav class="abs topbar">
    <div class="abs mail">
      <svg width="16" height="12" viewBox="0 0 16 12"><rect x="0.5" y="0.5" width="15" height="11" fill="none" stroke="#fff"/><path d="M0.5 0.5 L8 7 L15.5 0.5" fill="none" stroke="#fff"/></svg>
      info@klvtech.example
    </div>
    <div class="abs menu"><span>Home</span><span>About Us</span><span>Services</span><span>Solutions</span><span>Clients</span><span>Offices</span><span>Contact</span></div>
    <div class="abs quote">Get a Quote</div>
    <div class="abs phone">
      <svg width="14" height="14" viewBox="0 0 24 24"><path d="M6.6 10.8a15 15 0 0 0 6.6 6.6l2.2-2.2a1 1 0 0 1 1-.25 11.4 11.4 0 0 0 3.6.57 1 1 0 0 1 1 1V20a1 1 0 0 1-1 1A17 17 0 0 1 3 4a1 1 0 0 1 1-1h3.5a1 1 0 0 1 1 1c0 1.25.2 2.45.57 3.57a1 1 0 0 1-.25 1z" fill="#fff"/></svg>
      010-555-0142
    </div>
  </nav>
  <div class="abs subbar">
    <div class="abs tab" style="left:372px;width:147px">Managed Services</div>
    <div class="abs tab" style="left:524px;width:142px">Hosting Services</div>
    <div class="abs tab" style="left:681px;width:147px">Transportation</div>
  </div>
</header>

<section>
  <div class="abs hero" role="img" aria-label="Technology stock photo with warm orange glow"></div>
  <div class="abs hero-social"><span></span><span></span><span></span><span></span></div>
  <div class="abs hero-box">
    <h1>Most innovative and preferred<br>ICT and Engineering Company</h1>
    <p>KLV Technologies is committed to the fair and ethical treatment<br>of employees and stakeholders</p>
  </div>

  <div class="abs card" style="left:147px"><div class="art" role="img" aria-label="Server rack illustration"></div><h3>Managed Service</h3><em>Learn more</em></div>
  <div class="abs card" style="left:479px"><div class="art" role="img" aria-label="Cloud hosting illustration"></div><h3>Hosting Service</h3><em>Learn more</em></div>
  <div class="abs card" style="left:809px"><div class="art" role="img" aria-label="Laptop with traffic light and map pin illustration"></div><h3>Transportation</h3><em>Learn more</em></div>

  <h2 class="abs section-title" style="top:797px">Thought Behind KLV</h2>
  <p class="abs thought-copy">KLV Technologies was founded in 2013 as a Private Company. For Most of its initial existence, the company intends to establish close relationships with its various clients, with the intension of expanding throughout South Africa. KLV Technologies is dedicated to leveraging emerging technologies to provide the highest level of quality products and services, customer service, and security.</p>
</section>

<section class="abs governance"></section>
<h2 class="abs section-title" style="top:1038px">GOVERNANCE, RISK AND ETHICS</h2>
<p class="abs gov-copy">KLV Technologies understands investor concerns and issues of governance; ethics and sustainability which are also high on our agenda.<br>Our integrated approach includes uncompromising governance standards, adaptive risk management, a forwardthinking ethics policy and a dynamic approach to continued sustainability that sees us take an active leadership and development role in our operating communities.</p>

<div class="abs value" style="left:239px;top:1268px">INTEGRITY</div>
<p class="abs value-copy" style="left:508px;top:1349px;width:360px">We believe that all decisions are made with integrity, being honest with self and with others.</p>

<div class="abs value" style="left:737px;top:1541px">CUSTOMER<br>SERVICE</div>
<p class="abs value-copy" style="left:260px;top:1637px;width:420px">We believe that customers can and will take notice of and appreciate great, caring service. We base our efforts on this foundation.</p>

<div class="abs value" style="left:248px;top:1859px">CONTINUOUS<br>IMPROVEMENT</div>
<p class="abs value-copy" style="left:510px;top:1915px;width:400px">We believe in not accepting the status quo; we believe in the value of ongoing training in any form. We believe in providing opportunity for personal, professional, and organizational growth and innovation for our people and our company.</p>

<section>
  <h2 class="abs section-title" style="top:2234px">Our Partners</h2>
  <div class="abs partners-band"></div>
  <div class="abs badge" style="left:38px;width:168px"></div>
  <div class="abs badge" style="left:236px;width:128px"></div>
  <div class="abs badge" style="left:400px;width:165px"></div>
  <div class="abs badge" style="left:598px;width:100px"></div>
  <div class="abs badge" style="left:742px;width:110px"></div>
  <div class="abs badge" style="left:876px;width:148px"></div>
  <div class="abs badge" style="left:1058px;width:100px"></div>
</section>

<section class="abs competence"></section>
<h2 class="abs section-title" style="top:2551px">OUR COMPETENCIES AND CAPACITY</h2>
<p class="abs comp-lead" style="left:175px;top:2700px;width:470px">Our company possess years of ICT experience in varied fields such as:</p>
<ul class="abs comp-list" style="left:170px;top:2814px">
  <li>- ICT Company Setup and Management</li>
  <li>- ICT Infrastructure Built and Support</li>
  <li>- Hosted Environments</li>
  <li>- Applications Development and Maintenance</li>
  <li>- Network Deployment and Support</li>
  <li>- Managed Services and Software Sales and Support</li>
  <li>- Audio Visual Solutions</li>
</ul>
<div class="abs photo" style="left:751px;top:2693px;width:312px;height:312px;background:radial-gradient(circle at 65% 45%,#9ab8c8 0%,#3a5d72 35%,#10202c 75%)" role="img" aria-label="Digital globe with light trails"></div>

<div class="abs photo" style="left:179px;top:3151px;width:312px;height:312px;background:radial-gradient(circle at 50% 55%,#e8f3f8 0%,#9cc3d6 35%,#3a4a58 80%)" role="img" aria-label="Hand touching a glowing digital surface"></div>
<p class="abs comp-lead" style="left:617px;top:3162px;width:440px">Our resources have experiences in methodologies and principles in the following environments:</p>
<ul class="abs comp-list" style="left:617px;top:3280px">
  <li>- &nbsp;Project Management</li>
  <li>- &nbsp;Enterprise Management and Architecture</li>
  <li>- &nbsp;Business Analysis</li>
  <li>- &nbsp;Network Integration and Support</li>
  <li>- &nbsp;Systems Development</li>
</ul>

<section>
  <h2 class="abs write">Write To Us</h2>
  <p class="abs write-copy">Our company provides live support via telephone or through the Internet 24 hours a day, 7 days a week. You can speak to our Engineers if you have a roblem and the will fix most problems remotely, so that you can be back up and running without having to wait for a technician to come to your office. We can help with server, desktop and network issues.</p>
  <div class="abs form"></div>
  <div class="abs field" style="top:3651px">Name</div>
  <div class="abs field" style="top:3714px">Contact no.</div>
  <div class="abs field" style="top:3779px">Email</div>
  <div class="abs field" style="top:3847px;height:180px">Write your message here...</div>
</section>

<footer>
  <div class="abs footer"></div>
  <div class="abs brand foot-logo">
    <span class="brand-dot"></span>
    <span class="brand-text"><span class="name">KLV</span><span class="sub">TECHNOLOGIES</span></span>
  </div>
  <div class="abs foot-contact">info@klvtech.example<br>010-555-0142</div>
  <div class="abs foot-social"><span></span><span></span><span></span><span></span></div>
  <div class="abs region" style="left:514px;top:4152px">
    <h4>LIMPOPO</h4>
    <p>14 Ridgeway Street<br>Marloth Park<br>0811</p>
    <p>P. O. Box 40221<br>Fernhill<br>0813</p>
  </div>
  <div class="abs region" style="left:896px;top:4154px">
    <h4>GAUTENG</h4>
    <p>Building 5<br>8 Oakfield Drive<br>Brookdale<br>Westhaven<br>2061</p>
    <p>Po Box 382<br>Ashcombe<br>2067</p>
  </div>
  <div class="abs copyright">Copyright Reserved 2023</div>
</footer>

</body>
</html>
```